UI Design for a pre-ordering & Universal loyalty mobile app

We have built a central universal, preordering and gamification mobile app for alot of F&B merchant. The app is called PIXU (Pixoo as in eating something fast). Main goal for this app is too
1. Give users a universal loyalty system where they can accumulate loyalty points and use it on any brands
2. Gives user the ability to preorder for their food or drinks on the app and pick it up instore
3. There will be an E-wallet that is general or there can be a brand e-wallet (where they top-up with the brand only and get extra bonus)
4. There will be promotion such as games, top-up bonuses and rewards.
5. Community app where they can send money or promotion to their friends and will be able to play games together
This app is developed on the Flutter framework and also uses fontawesome font/icon package. Please consider this when doing the UI design for the app.
We are planning to create a mascot for our app as well and when it comes to color and icon, it's not set in stone and we are open for ideas.
I will attached our app icon and a few of our screens for your reference and each page details as follows:
Navigation bar.
There is a navigation bar on the top that should be visible on all screen. On the left will be a button to enter the menu which gives user more option and on the right will be a place for them to scan their QR code for loyalty points or payment and also a button to access their e-wallet.
1. Home screen
This screen is basically the main screen after user login. In this screen there will be
- Main banner (main promotions that's controlled by us)
- Specials banner (smaller) that will be controlled by the store/brands
- Favourite Store or Favourite food/drinks that user pre-configure
2. Shop screen (or can be called something else)
This screen is where they can browse all our participating stores. This screen will include
- Categories (filter)
- Brands which user can click and only view the brand page and stores
- All stores sorted by distances
3. Brand screen
The brand screen gives our brand with multiple store a presense on the app that is branded for them. They can have their own color scheme, logo and will only display their own store
4. Store screen
This will display all the store details, opening time, location, contact information etc.
- This screen will contain a banner/store image
- Store details
- Categories
- Food/drinks within the category
5. Order history screen
This will display their current order or their past order. Not sure if it should be on the main navigation or the sub navigation.
When making the UI design, please work on a color theme that will suit and also consider a mascot design in the future.
Feel free to ask me any questions before proceeding.
Thanks

```html
<!DOCTYPE html>
<html lang="en">
<head>
<meta charset="utf-8">
<title>Home – Food Pre-order</title>
<link rel="stylesheet" href="https://fonts.googleapis.com/css2?family=Poppins:wght@400;500;600;700&display=swap">
<style>
  :root{
    --ink:#1d1d1f;
    --ink-soft:#4a4a4f;
    --muted:#8b8b92;
    --accent-blue:#3a93d8;
    --accent-pink:#e2235f;
    --lime:#97cd3b;
    --surface:#ffffff;
    --card-shadow:rgba(0,0,0,0.08);
    --glass:rgba(255,255,255,0.22);
    --glass-dark:rgba(40,40,40,0.55);
    --nav-pill:#222222;
  }
  *{box-sizing:border-box;margin:0;padding:0}
  html,body{width:1200px;height:3210px;overflow:hidden;background:var(--surface)}
  body{font-family:'Poppins',sans-serif;color:var(--ink)}
  .screen{position:relative;width:360px;height:963px;transform:scale(3.33334);transform-origin:0 0;overflow:hidden;background:var(--surface)}
  .abs{position:absolute}

  .avatar{left:20px;top:20px;width:46px;height:46px;border-radius:50%;background:linear-gradient(160deg,#c9d6e2,#7f95a8)}
  .greeting{left:76px;top:21px;font-size:10px;color:var(--muted)}
  .user-name{left:76px;top:34px;font-size:20px;font-weight:700;line-height:1.2}
  .top-icon{top:31px;width:24px;height:24px}

  .hero{left:20px;top:86px;width:320px;height:248px;border-radius:20px;overflow:hidden;
        background:radial-gradient(ellipse at 55% 45%,#c99a52 0%,#8a6a3a 28%,#3a3d3b 60%,#232726 100%)}
  .hero-caption{left:10px;top:174px;width:300px;height:64px;border-radius:16px;background:var(--glass);
        border:1px solid rgba(255,255,255,0.25);backdrop-filter:blur(6px)}
  .hero-title{left:20px;top:13px;color:#fff;font-size:15.5px;font-weight:600;line-height:1.3}
  .hero-arrow{left:244px;top:14px;width:36px;height:36px;border-radius:50%;background:rgba(255,255,255,0.3);display:flex;align-items:center;justify-content:center}

  .dot{top:348px;height:6px;width:6px;border-radius:3px;background:#cfcfd4}
  .dot.active{width:24px;background:var(--accent-blue)}

  .section-title{left:20px;font-size:16px;font-weight:600}
  .see-all{left:300px;font-size:12px;font-weight:500;color:var(--accent-blue)}

  .deal-card{top:413px;width:180px;height:160px;border-radius:20px;background:var(--surface);box-shadow:0 4px 14px var(--card-shadow);overflow:hidden}
  .deal-photo{left:0;top:0;width:180px;height:110px;border-radius:20px}
  .deal-name{left:10px;top:118px;font-size:12px;font-weight:600;color:var(--ink-soft);line-height:1.35;width:110px}
  .deal-badge{left:115px;top:124px;height:22px;padding:0 9px;border-radius:11px;background:var(--accent-pink);color:#fff;font-size:10px;font-weight:600;line-height:22px}

  .fav-card{top:634px;width:280px;height:172px;border-radius:20px;overflow:hidden}
  .bonus-tag{left:146px;top:11px;width:124px;height:28px;border-radius:10px;background:var(--glass-dark);color:#fff;font-size:10px;font-weight:600;line-height:28px;text-align:center}
  .stat{top:142px;height:20px;border-radius:10px;padding:0 8px;display:flex;align-items:center;gap:4px;font-size:8px;color:#fff;border:1px solid rgba(255,255,255,0.6)}
  .stat.rating{background:var(--accent-pink);border-color:var(--accent-pink)}

  .brand-mark{top:822px;width:34px;height:34px;border-radius:50%}
  .brand-name{left:74px;top:820px;font-size:14px;font-weight:600;color:var(--ink-soft)}
  .brand-sub{left:74px;top:840px;font-size:10px;color:var(--muted)}
  .brand-go{left:264px;top:826px;width:26px;height:26px;border-radius:50%;background:var(--accent-blue);display:flex;align-items:center;justify-content:center}

  .tab-bar{left:20px;top:883px;width:320px;height:60px;border-radius:30px;background:var(--lime)}
  .tab-home{left:10px;top:10px;width:89px;height:40px;border-radius:20px;background:var(--nav-pill);color:#fff;font-size:10px;font-weight:500;display:flex;align-items:center;justify-content:center;gap:8px}
  .tab-icon{top:18px;width:24px;height:24px}
</style>
</head>
<body>
<main class="screen">

  <div class="abs avatar" role="img" aria-label="Profile photo of the user"></div>
  <p class="abs greeting">Good morning,</p>
  <h1 class="abs user-name">Rohan</h1>

  <svg class="abs top-icon" style="left:272px" viewBox="0 0 24 24" fill="none" stroke="#333" stroke-width="1.6" stroke-linecap="round" aria-label="Scan">
    <path d="M3 8V5a2 2 0 0 1 2-2h3M16 3h3a2 2 0 0 1 2 2v3M21 16v3a2 2 0 0 1-2 2h-3M8 21H5a2 2 0 0 1-2-2v-3"/>
    <rect x="7" y="7" width="4" height="4" rx="1"/><rect x="13" y="7" width="4" height="4" rx="1"/>
    <rect x="7" y="13" width="4" height="4" rx="1"/><rect x="13" y="13" width="4" height="4" rx="1"/>
  </svg>
  <svg class="abs top-icon" style="left:314px" viewBox="0 0 24 24" fill="none" stroke="#333" stroke-width="1.6" stroke-linejoin="round" aria-label="Wallet">
    <path d="M4 7a2 2 0 0 1 2-2h10v3"/><rect x="4" y="8" width="16" height="11" rx="2.5"/><path d="M20 11h-4a2 2 0 0 0 0 4h4"/>
  </svg>

  <section class="abs hero" role="img" aria-label="Stack of pancakes with banana and syrup on a dark table">
    <div class="abs hero-caption">
      <h2 class="abs hero-title">15 Places for<br>Bingeworthy Desserts</h2>
      <div class="abs hero-arrow">
        <svg width="18" height="18" viewBox="0 0 24 24" fill="none" stroke="#fff" stroke-width="2" stroke-linecap="round" stroke-linejoin="round"><path d="M4 12h16M14 6l6 6-6 6"/></svg>
      </div>
    </div>
  </section>

  <span class="abs dot" style="left:156px"></span>
  <span class="abs dot active" style="left:168px"></span>
  <span class="abs dot" style="left:198px"></span>

  <h3 class="abs section-title" style="top:375px">Deals</h3>
  <a class="abs see-all" style="top:377px">See all</a>

  <article class="abs deal-card" style="left:20px">
    <div class="abs deal-photo" role="img" aria-label="Grilled skewers and sauces on a wooden board" style="background:linear-gradient(135deg,#6b4a33,#a0643c 45%,#3d3a36)"></div>
    <p class="abs deal-name">Phasellus a vulputate</p>
    <span class="abs deal-badge">25% Off</span>
  </article>
  <article class="abs deal-card" style="left:214px">
    <div class="abs deal-photo" role="img" aria-label="Nachos with dips on a wooden platter" style="background:linear-gradient(135deg,#8a6a48,#d0a25c 45%,#5c4a3a)"></div>
    <p class="abs deal-name">Vestibulum elit dolor</p>
    <span class="abs deal-badge">25% Off</span>
  </article>

  <h3 class="abs section-title" style="top:596px">Favorites</h3>
  <a class="abs see-all" style="top:598px">See all</a>

  <article class="abs fav-card" style="left:20px;background:linear-gradient(170deg,#2a2624,#4a3a34 45%,#6e5550 70%,#241f1d)" role="img" aria-label="Dimly lit restaurant dining room with set tables">
    <span class="abs bonus-tag">100% Deposit Bonus</span>
    <span class="abs stat rating" style="left:10px">
      <svg width="10" height="10" viewBox="0 0 24 24" fill="#fff"><path d="M12 21s-8-5.2-8-11a4.5 4.5 0 0 1 8-2.8A4.5 4.5 0 0 1 20 10c0 5.8-8 11-8 11z"/></svg>4.8</span>
    <span class="abs stat" style="left:60px">
      <svg width="10" height="10" viewBox="0 0 24 24" fill="none" stroke="#fff" stroke-width="2"><path d="M12 21s-7-6.5-7-12a7 7 0 0 1 14 0c0 5.5-7 12-7 12z"/><circle cx="12" cy="9" r="2.5"/></svg>1 km</span>
    <span class="abs stat" style="left:112px">
      <svg width="10" height="10" viewBox="0 0 24 24" fill="none" stroke="#fff" stroke-width="2" stroke-linecap="round"><circle cx="12" cy="12" r="9"/><path d="M12 7v5l3 2"/></svg>2 min</span>
  </article>
  <article class="abs fav-card" style="left:314px;background:linear-gradient(170deg,#5f8fa8,#2f6f7e 50%,#3b3a36)" role="img" aria-label="Seaside cafe terrace">
    <span class="abs stat rating" style="left:6px">
      <svg width="10" height="10" viewBox="0 0 24 24" fill="#fff"><path d="M12 21s-8-5.2-8-11a4.5 4.5 0 0 1 8-2.8A4.5 4.5 0 0 1 20 10c0 5.8-8 11-8 11z"/></svg>4.2</span>
  </article>

  <span class="abs brand-mark" style="left:30px;background:#d52b1e"></span>
  <p class="abs brand-name">Burger Barn</p>
  <p class="abs brand-sub">Ornare nec nulla vitae</p>
  <span class="abs brand-go">
    <svg width="14" height="14" viewBox="0 0 24 24" fill="none" stroke="#fff" stroke-width="2.2" stroke-linecap="round" stroke-linejoin="round"><path d="M5 12h14M13 6l6 6-6 6"/></svg>
  </span>
  <span class="abs brand-mark" style="left:324px;background:#1f6b4a"></span>

  <nav class="abs tab-bar">
    <div class="abs tab-home">
      <svg width="20" height="20" viewBox="0 0 24 24" fill="none" stroke="#fff" stroke-width="1.6" stroke-linejoin="round"><path d="M4 10.5 12 4l8 6.5V20H4z"/></svg>
      Home
    </div>
    <svg class="abs tab-icon" style="left:131px" viewBox="0 0 24 24" fill="none" stroke="#222" stroke-width="1.6" stroke-linecap="round" stroke-linejoin="round" aria-label="Shop"><path d="M5 9h14l-1.2 10a2 2 0 0 1-2 1.8H8.2a2 2 0 0 1-2-1.8z"/><path d="M9 9V7a3 3 0 0 1 6 0v2M9.5 14h.01M14.5 14h.01"/></svg>
    <svg class="abs tab-icon" style="left:200px" viewBox="0 0 24 24" fill="none" stroke="#222" stroke-width="1.6" stroke-linecap="round" stroke-linejoin="round" aria-label="Orders"><path d="M6 20V5a2 2 0 0 1 2-2h10a2 2 0 0 1 2 2v4h-4"/><path d="M16 3a2 2 0 0 1 2 2M6 20l2-1.5 2 1.5 2-1.5V9M10 8h3M10 12h2"/></svg>
    <svg class="abs tab-icon" style="left:272px" viewBox="0 0 24 24" fill="none" stroke="#222" stroke-width="1.6" stroke-linecap="round" stroke-linejoin="round" aria-label="Rewards"><path d="M4 7l4 4 4-6 4 6 4-4v12H4z"/></svg>
  </nav>

</main>
</body>
</html>
```